New Brochures to deliver confidence of our company to our customers

I would like to have new brochure to be used to distribute to our prospective customers besides the power point presentation. I like the powerpoint you did for us and would like to follow the direction that you have set up. I will attach a number of photos for you to include in our brochure for you to choose. I like the brochure to be modern and forward thinking but just practical. The brochure needs to have three languages which are English, Chinese and Japanese. Attaches is the power point that we like.

Target Market(s)

Multinational companies

Industry/Entity Type

Electronics

Colors

Designer to choose colors to be used in the design.

Requirements
Must have
• Feel lively and modern and yet giving people a sense of confidence. Highlighting the automation is important. Can let us know if you want more photos. The brochure will have three languages, namely english, japanese and chinese.

```html
<!DOCTYPE html>
<html lang="en">
<head>
<meta charset="utf-8">
<title>Norcel Circuit Limited – Brochure</title>
<link rel="stylesheet" href="https://fonts.googleapis.com/css2?family=Open+Sans:wght@400;600;700&display=swap">
<style>
:root{
  --stage:#c9c9c9;
  --paper:#f1f1f1;
  --ink:#333a3c;
  --ink-soft:#4c5457;
  --teal-deep:#06262a;
  --teal-dark:#0a3438;
  --teal:#0e7b7d;
  --teal-head:#0f6a6c;
  --teal-bright:#1fb0ad;
  --cyan:#3de6e0;
  --green:#1f7a45;
  --row-a:#dcdcdc;
  --row-b:#cbcbcb;
  --white:#ffffff;
}
*{margin:0;padding:0;box-sizing:border-box}
html,body{width:830px;height:1200px;overflow:hidden}
body{background:var(--stage);font-family:"Open Sans",Arial,sans-serif;color:var(--ink);position:relative}

.spread{position:absolute;left:35px;width:760px;display:flex;box-shadow:0 2px 6px rgba(0,0,0,.25)}
.spread--cover{top:42px;height:538px;background:var(--paper);overflow:hidden}
.spread--inside{top:622px;height:538px}

/* cover */
.cover-art{position:absolute;inset:0}
.contact{position:absolute;left:30px;top:38px;font-size:8.3px;line-height:12px;color:var(--ink)}
.contact__name{color:var(--teal-head);font-weight:700;font-size:9px;margin-bottom:9px}
.contact__address{margin-bottom:6px}
.contact__label{color:var(--teal-head);font-weight:700;display:inline-block;width:11px}
.brand{position:absolute;text-align:center}
.brand__name{font-weight:700;letter-spacing:4px;line-height:1}
.brand__tagline{font-weight:600;letter-spacing:1.6px;white-space:nowrap}
.brand--top{left:455px;top:58px;width:228px}
.brand--top .brand__name{font-size:58px;color:#1e1e1e;border-bottom:1.5px solid #1e1e1e;padding-bottom:4px}
.brand--top .brand__tagline{font-size:9.2px;color:#1e1e1e;margin-top:4px}
.brand--bottom{left:218px;top:468px;width:122px}
.brand--bottom .brand__name{font-size:30px;color:var(--white);border-bottom:1px solid var(--white);padding-bottom:2px}
.brand--bottom .brand__tagline{font-size:5px;color:var(--white);letter-spacing:.9px;margin-top:2px}

/* inside */
.panel{width:380px;height:100%;position:relative}
.panel--light{background:var(--paper);padding:22px 24px 0 24px}
.panel--dark{background:linear-gradient(180deg,var(--teal-deep),#092c30 60%,var(--teal-deep));color:#e5f1f1;padding:22px 22px 0 26px}
.section-title{font-size:12.2px;font-weight:700;color:var(--teal-head);margin-bottom:12px}
.panel--dark .section-title{color:var(--teal-bright)}
.body-text{font-size:7.4px;line-height:10.6px;margin-bottom:10px;color:var(--ink-soft)}
.panel--dark .body-text{color:#d8e6e6}

.share-table{width:329px;border-collapse:collapse;font-size:7.4px;margin:12px 0 20px}
.share-table th{background:var(--teal);color:var(--white);text-align:left;font-weight:700;height:17px;padding-left:9px}
.share-table td{height:17px;padding-left:9px;font-weight:700;color:#3a3a3a}
.share-table tr:nth-child(odd) td{background:var(--row-a)}
.share-table tr:nth-child(even) td{background:var(--row-b)}
.share-table .col-app{width:206px}

.factory-photo{position:absolute;left:0;top:165px;width:380px;height:92px;background:linear-gradient(90deg,#8e9a98,#c9cfca 35%,#9aa5a3 60%,#d4d8d4);}
.customers{position:absolute;left:26px;top:268px;right:22px}
.customer-board{position:absolute;left:24px;top:336px;width:332px;height:177px;background:var(--white);padding:14px 12px;display:grid;grid-template-columns:repeat(5,1fr);grid-template-rows:repeat(4,1fr);gap:4px 5px}
.customer{border:1px solid #e2e2e2;border-radius:4px;display:flex;align-items:center;justify-content:center;font-size:7.6px;font-weight:700;color:#2f3436;text-align:center}
</style>
</head>
<body>

<section class="spread spread--cover">
  <svg class="cover-art" width="760" height="538" viewBox="0 0 760 538" aria-hidden="true">
    <defs>
      <linearGradient id="dark" x1="0" y1="0" x2="0" y2="1">
        <stop offset="0" stop-color="#0a3236"/>
        <stop offset="1" stop-color="#062124"/>
      </linearGradient>
      <radialGradient id="glow" cx="0.5" cy="0.5" r="0.5">
        <stop offset="0" stop-color="#2fd9d3" stop-opacity=".45"/>
        <stop offset="1" stop-color="#2fd9d3" stop-opacity="0"/>
      </radialGradient>
      <linearGradient id="traceFaint" x1="0" y1="0" x2="1" y2="1">
        <stop offset="0" stop-color="#d8d8d8"/>
        <stop offset="1" stop-color="#ececec"/>
      </linearGradient>
    </defs>
    <rect width="760" height="538" fill="#f1f1f1"/>
    <rect x="170" y="0" width="210" height="200" fill="url(#traceFaint)" opacity=".5" role="img" aria-label="Faint circuit trace pattern"/>
    <rect x="0" y="160" width="200" height="230" fill="url(#traceFaint)" opacity=".5" role="img" aria-label="Faint circuit trace pattern"/>
    <path d="M0,372 C90,470 220,430 330,320 C420,230 560,205 760,222 L760,538 L0,538 Z" fill="#b5b5b5"/>
    <path d="M0,395 C100,470 230,420 340,315 C430,235 570,212 760,232 L760,538 L0,538 Z" fill="url(#dark)"/>
    <path d="M580,206 C650,210 720,222 760,240 L760,252 C720,232 650,218 580,206 Z" fill="#1f7a45"/>
    <line x1="380" y1="230" x2="380" y2="538" stroke="#0d3a3e" stroke-width="1"/>
    <ellipse cx="590" cy="390" rx="150" ry="150" fill="url(#glow)" role="img" aria-label="Glowing cyan circuit-tree illustration"/>
    <ellipse cx="290" cy="370" rx="95" ry="85" fill="url(#glow)" role="img" aria-label="Cyan circuit traces rising along the wave"/>
  </svg>

  <div class="contact">
    <p class="contact__name">Norcel Circuit Limited</p>
    <p class="contact__address">12/F Kestrel Tower<br>88 Marlow Avenue<br>Kestrel Bay, HONG KONG</p>
    <p><span class="contact__label">T:</span> (852)2610 4480<br>
       <span class="contact__label">F:</span> (852)2610 4481<br>
       <span class="contact__label">E:</span> sales@norcelcircuit.com</p>
  </div>

  <div class="brand brand--top">
    <p class="brand__name">NCL</p>
    <p class="brand__tagline">Printed Circuit Boards is Our Business</p>
  </div>
  <div class="brand brand--bottom">
    <p class="brand__name">NCL</p>
    <p class="brand__tagline">Printed Circuit Boards is Our Business</p>
  </div>
</section>

<section class="spread spread--inside">
  <div class="panel panel--light">
    <h2 class="section-title">NCL Background</h2>
    <p class="body-text">Established in 2007, Norcel Circuit Limited (NCL) is a Hong Kong company specializing in single and double sized printed circuit boards. Its manufacturing facility is located in a self-owned facility in Linshan Township, South China which is 50 minutes from Hong Kong.</p>
    <p class="body-text">Our mission is to becomea premium low costs PCB supplierthat fully embraces human, social and environmental responsibilities.</p>
    <p class="body-text">Through our insatiable drive to maximize efficiency, NCL is becoming a highly efficient PCB factory with a capacity of 140,000 sq meter a month.</p>
    <p class="body-text">PCB is our business and it is through continued automation and innovation that will drive our growth in the next 10 years</p>

    <h2 class="section-title" style="margin-top:16px">Single Layered Printed Circuit Boards</h2>
    <p class="body-text">We are offering single layered circuit boards through our own production facility in China for customers in the following industries:</p>
    <table class="share-table">
      <thead><tr><th class="col-app">Application</th><th>Proportion</th></tr></thead>
      <tbody>
        <tr><td>Household Appliances</td><td>60%</td></tr>
        <tr><td>Power Supply</td><td>20%</td></tr>
        <tr><td>Lighting Control System</td><td>10%</td></tr>
        <tr><td>Others</td><td>10%</td></tr>
      </tbody>
    </table>

    <h2 class="section-title">Double Layered &amp; Multi-layered Printed Circuit Boards</h2>
    <p class="body-text">We are offering two layered and multi-layered circuit boards for our customers through our strategically approved printed circuit boards manufacturers.</p>
    <p class="body-text">With our own UL for double sided and multi-layered circuit boards, we work with a number of strategically approved manufacturers in delivering 100% quality guaranteed printed circuit boards for our customers.</p>
    <p class="body-text">All the PCBs are inspected by our own Automatic Visual Inspection (AVI) Machine before we deliver to customers. We perform comprehensive quality and environmental audit of our manufacturers on quarterly and annual basis.</p>
  </div>

  <div class="panel panel--dark">
    <h2 class="section-title">Our Investment &amp; Upgrade</h2>
    <p class="body-text">Maintaining a highly automated factory is the only way to ensure consistent product and long term competitive efficiency.</p>
    <p class="body-text">From 2015 to 2017, NCL invested over US$3.5 million in automating our production and quality control process and enhancing our environmental processing facility. We will spend a further US$1.5 million in 2018 to continue our improvement process to ensure we are one of the most efficient and highest quality single sided PCB manufacturers in Asia. By the end of 2018, 100% of our PCBs will be inspected by AVI before they are delivered to our customers.</p>

    <div class="factory-photo" role="img" aria-label="Photo of automated PCB production machinery on the factory floor"></div>

    <div class="customers">
      <h2 class="section-title">Our Main Customers</h2>
      <p class="body-text">NCL is embracing a philosophy of being a partner with our customers. As a result, we are strategic PCB suppliers to the following world renowned companies:</p>
    </div>

    <div class="customer-board">
      <div class="customer">Voltaro</div>
      <div class="customer">Kessmar</div>
      <div class="customer">Brightwell</div>
      <div class="customer">Nordaxis</div>
      <div class="customer">Plastiva</div>
      <div class="customer">Orvello</div>
      <div class="customer">Lumecor</div>
      <div class="customer">Tarvik</div>
      <div class="customer">Halden</div>
      <div class="customer">Corvex</div>
      <div class="customer">Ampliva</div>
      <div class="customer">Visterra</div>
      <div class="customer">Deltrane</div>
      <div class="customer">Kentra</div>
      <div class="customer">Brava Motion</div>
      <div class="customer">Arvelo</div>
      <div class="customer">Hylon</div>
      <div class="customer">Ecovanta</div>
      <div class="customer">Holt &amp; Tan</div>
      <div class="customer">Quintara</div>
    </div>
  </div>
</section>

</body>
</html>
```